Infographic ranking standards for countries

I have collected various rearing standards for animal welfare from various countries - such as How Much Space Animals Are Given (stocking density); Rest Hours per day; Permissible slaughter methods; Air quality limits (ammonia %), etc. I want to show how each country ranks in comparison in a visual interesting way. Graphs in excel or Smart Art are too boring. Information needs to be clear for those people looking for it and presented in a new appealing way. I was thinking stocking density could be presented by the Pigs able to turn around (vs. too crowded) or being degree to which hens could spread wings. Dark period as the size of a moon vs. sun to indicate rest opportunity. These might be terrible ideas so I am very open. Just want a way to visualize the differences. Open to using flags of countries too and some specific Animal Welfare logos would need to be added. I am looking for a mock up for style and then I can give you the data. Overall, I would need information for about 5 standards for chickens done fairly quickly (4 days) but afterwords, this would be an on-going project for all species and all standards. Here is an example of stocking density for meat chickens.

Sweden - 20kg/m2 to 36 kg/m2 depending on welfare program results. Most rearing at 36kg/m2.

Switzerland - 30 kg/m2

Thailand - 33kg/m2

Scotland - 34kg/m2

Canada - 31-38kg/m2

USA - 36kg to 42kg/m2 depends on bird market weight

Brazil - 30-38(39)kg/m2 (study showed relative to climate - 30low, 34mid, 38high)

European Union - 33kg/m2 up to 39kg/m2 (or 42kg/m2) after meeting certain conditions

England - 33kg/m2 up to 39kg/m2 (or 42kg/m2) after meeting certain conditions

South Africa - 40kg/m2

```html
<!DOCTYPE html>
<html lang="en">
<head>
<meta charset="utf-8">
<title>Stocking Density in kg/m2</title>
<link href="https://fonts.googleapis.com/css2?family=Nunito+Sans:wght@400;600;700&display=swap" rel="stylesheet">
<style>
  :root{
    --ink:#4a4a4a;
    --muted:#8a8a8a;
    --accent:#29abe2;
    --accent-dark:#1b6f99;
    --icon-faint:#cfd3d6;
    --map-grey:#9c9c9c;
    --line:#6d6d6d;
    --bg:#ffffff;
  }
  *{margin:0;padding:0;box-sizing:border-box}
  html,body{width:1200px;height:938px;overflow:hidden;background:var(--bg)}
  body{font-family:"Nunito Sans",sans-serif;color:var(--ink);position:relative}
  .title{position:absolute;left:49px;top:28px;font-size:56px;font-weight:600;letter-spacing:-0.5px;color:var(--ink)}
  .subtitle{position:absolute;left:404px;top:97px;font-size:22px;font-weight:600;color:var(--muted)}

  .world-map{position:absolute;left:176px;top:245px;width:884px;height:515px;border-radius:40px;
    background:radial-gradient(ellipse at 35% 40%, #7fc4e8 0%, #a5a5a5 35%, var(--map-grey) 70%);opacity:.9}

  .connectors{position:absolute;left:0;top:0;width:1200px;height:938px;pointer-events:none}
  .connectors polyline{fill:none;stroke:var(--line);stroke-width:1}
  .connectors circle{fill:#555}

  .country{position:absolute}
  .country .name{display:inline-block;font-size:16.5px;font-weight:700;color:var(--ink);vertical-align:middle}
  .country .star{color:var(--accent)}
  .country .value{position:absolute;font-size:14px;color:var(--ink);white-space:nowrap}
  .rating{display:inline-flex;gap:5px;margin-left:10px;vertical-align:middle}
  .rating i{width:19px;height:19px;border-radius:50% 50% 50% 8px;background:var(--accent);display:block}
  .rating i.part{background:linear-gradient(90deg,var(--accent) 45%,var(--icon-faint) 45%)}

  .flag{position:absolute;width:28px;height:28px;border-radius:50%;overflow:hidden;border:1px solid #ddd}
  .flag-ch{background:#e52421}
  .flag-ch::before{content:"";position:absolute;left:11px;top:5px;width:6px;height:18px;background:#fff}
  .flag-ch::after{content:"";position:absolute;left:5px;top:11px;width:18px;height:6px;background:#fff}
  .flag-se{background:#1f5ca8}
  .flag-se::before{content:"";position:absolute;left:8px;top:0;width:5px;height:28px;background:#f6c900}
  .flag-se::after{content:"";position:absolute;left:0;top:11px;width:28px;height:5px;background:#f6c900}
  .flag-sc{background:#1f5ca8}
  .flag-gb{background:linear-gradient(#fff 40%,#d8232a 40% 60%,#fff 60%);}
  .flag-gb::before{content:"";position:absolute;left:11px;top:0;width:6px;height:28px;background:#d8232a}
  .flag-ca{background:linear-gradient(90deg,#d8232a 26%,#fff 26% 74%,#d8232a 74%)}
  .flag-us{background:repeating-linear-gradient(#c8102e 0 3px,#fff 3px 6px)}
  .flag-us::before{content:"";position:absolute;left:0;top:0;width:13px;height:13px;background:#2b3f87}
  .flag-th{background:linear-gradient(#d8232a 17%,#fff 17% 33%,#2b3f87 33% 67%,#fff 67% 83%,#d8232a 83%)}
  .flag-br{background:#2a9d3f}
  .flag-br::before{content:"";position:absolute;left:5px;top:5px;width:18px;height:18px;background:#f6c900;transform:rotate(45deg) scale(.8)}
  .flag-br::after{content:"";position:absolute;left:9px;top:9px;width:10px;height:10px;border-radius:50%;background:#2b3f87}
  .flag-za{background:linear-gradient(#d8232a 33%,#fff 33% 38%,#1e8a3e 38% 62%,#fff 62% 67%,#2b3f87 67%)}
  .flag-za::before{content:"";position:absolute;left:0;top:6px;width:10px;height:16px;background:#111}
  .flag-eu{background:#2b3f87}
  .flag-eu::before{content:"";position:absolute;left:6px;top:6px;width:16px;height:16px;border-radius:50%;border:2px dotted #f6c900}

  .legend{position:absolute;left:39px;top:830px;font-size:12.5px;font-weight:700;color:var(--accent)}
  .legend .rating{margin:0 8px 0 0}
  .note{position:absolute;left:39px;font-size:12px;font-weight:700}
  .note-one{top:864px;color:var(--accent)}
  .note-two{top:886px;color:var(--accent-dark)}
</style>
</head>
<body>
  <h1 class="title">Stocking Density</h1>
  <p class="subtitle">in kg/m2</p>

  <div class="world-map" role="img" aria-label="World map with the compared countries highlighted in shades of blue"></div>

  <svg class="connectors" viewBox="0 0 1200 938" aria-hidden="true">
    <polyline points="920,160 680,160 680,455 592,449"/><circle cx="592" cy="449" r="4"/>
    <polyline points="131,211 365,211 580,428"/><circle cx="580" cy="428" r="4"/>
    <polyline points="610,233 610,432 585,440"/><circle cx="585" cy="440" r="4"/>
    <polyline points="942,251 670,251 640,390"/><circle cx="640" cy="390" r="4"/>
    <polyline points="128,293 258,293 300,412"/><circle cx="300" cy="412" r="4"/>
    <polyline points="150,546 305,546 348,479"/><circle cx="348" cy="479" r="4"/>
    <polyline points="1120,539 890,539 845,562"/><circle cx="845" cy="562" r="4"/>
    <polyline points="150,686 366,686 450,624"/><circle cx="450" cy="624" r="4"/>
    <polyline points="660,760 648,685"/><circle cx="648" cy="685" r="4"/>
    <polyline points="575,824 638,824 638,470"/><circle cx="638" cy="470" r="4"/>
  </svg>

  <div class="country" style="left:718px;top:130px">
    <span class="name">England</span>
    <span class="rating"><i></i><i></i><i></i><i></i></span>
    <span class="value" style="left:0;top:40px">39kg/m2</span>
  </div>
  <span class="flag flag-gb" style="left:947px;top:146px"></span>

  <span class="flag flag-ch" style="left:74px;top:197px"></span>
  <div class="country" style="left:127px;top:184px">
    <span class="name">Switzerland</span>
    <span class="rating"><i></i><i></i><i></i></span>
    <span class="value" style="left:4px;top:38px">30 kg/m2</span>
  </div>

  <span class="flag flag-sc" style="left:410px;top:215px"></span>
  <div class="country" style="left:450px;top:204px">
    <span class="name">Scotland</span>
    <span class="rating"><i></i><i></i><i></i><i class="part"></i></span>
    <span class="value" style="left:36px;top:34px">34 kg/m2</span>
  </div>

  <div class="country" style="left:707px;top:221px">
    <span class="name">Sweden<span class="star">**</span></span>
    <span class="rating"><i></i><i></i><i></i><i class="part"></i></span>
    <span class="value" style="left:2px;top:40px">36 kg/m2</span>
  </div>
  <span class="flag flag-se" style="left:947px;top:237px"></span>

  <span class="flag flag-ca" style="left:74px;top:275px"></span>
  <div class="country" style="left:111px;top:265px">
    <span class="name">Canada</span>
    <span class="rating"><i></i><i></i><i></i><i class="part"></i></span>
    <span class="value" style="left:0;top:40px">38 kg/m2</span>
  </div>

  <span class="flag flag-us" style="left:91px;top:530px"></span>
  <div class="country" style="left:132px;top:518px">
    <span class="name">USA</span>
    <span class="rating"><i></i><i></i><i></i><i></i><i class="part"></i></span>
    <span class="value" style="left:0;top:41px">40 kg/m2</span>
  </div>

  <div class="country" style="left:927px;top:513px">
    <span class="name">Thailand</span>
    <span class="rating"><i></i><i></i><i></i><i class="part"></i></span>
    <span class="value" style="left:34px;top:36px">33 kg/m2</span>
  </div>
  <span class="flag flag-th" style="left:1117px;top:525px"></span>

  <span class="flag flag-br" style="left:91px;top:672px"></span>
  <div class="country" style="left:138px;top:653px">
    <span class="name">Brazil</span>
    <span class="rating"><i></i><i></i><i></i><i></i></span>
    <span class="value" style="left:0;top:50px">39kg/m2</span>
  </div>

  <div class="country" style="left:670px;top:735px">
    <span class="name">South Africa</span>
    <span class="rating"><i></i><i></i><i></i><i></i></span>
    <span class="value" style="left:0;top:40px">40 kg/m2</span>
  </div>
  <span class="flag flag-za" style="left:880px;top:748px"></span>

  <span class="flag flag-eu" style="left:343px;top:804px"></span>
  <div class="country" style="left:383px;top:793px">
    <span class="name">European Union<span class="star">*</span></span>
    <span class="rating"><i></i><i></i><i></i><i></i></span>
    <span class="value" style="left:0;top:34px">39kg/m2</span>
  </div>

  <div class="legend"><span class="rating"><i></i></span>10 kg/m2</div>
  <p class="note note-one">*if conditions met, earned from 33, up to 42</p>
  <p class="note note-two">**if conditions met, earned from 20</p>
</body>
</html>
```